Copper Ladle, Wine Bar and Bistro

We need a logo and business cards that reflects our wine bar concept. Please refer to the description below.Anthropologist and attorney Maren Holt Pravecky and attorney Dana Rueckl, in consultation with Executive Chef and restauranteur Oren Pask, seek to open Copper Ladle, a wine bar and bistro in the business district of Swarthmore Borough. Our concept, “Tasting Culture Through Wine”, brings together unique, delicious wines from around the world and regional small plates to locals eager to learn about and experience the gustatory joys of lesser known wine-producing locales.Strategically located in downtown Swarthmore, Pennsylvania, near the commuter train, Copper Ladle will be a comfortable, welcoming atmosphere in which to learn about, taste and enjoy interesting wines, dine, meet friends or just have a drink after work. After hours desserts, coffees, teas and other non-alcoholic beverages will be highly attractive to not only town residents but also the nearly 1600 college-aged students who attend Gladwick College.
Target Market(s)
People interested in learning about unusual wine regions. Design must capture small, local, village feel. Think of a family owned vineyard in a small corner of the world that produces great regional wine. Also, design should capture learning, education and taking in new experiences.
Contact Information for Business Card
CopperLadleDenholt.com
Logo Text
Copper Ladle
Colors
Designer to choose colors to be used in the design.
Requirements
Must have
- Small village feel.
Nice to have
- Vines. Grapes. Globe. Try greens and purples.

```html
<!DOCTYPE html>
<html lang="en">
<head>
<meta charset="utf-8">
<title>Copper Ladle — Business Card</title>
<link rel="stylesheet" href="https://fonts.googleapis.com/css2?family=Quicksand:wght@400;500;700&display=swap">
<style>
  :root {
    --backdrop: #e9e6e2;
    --card: #ffffff;
    --ink: #1c1c1c;
    --wine: #8c1d55;
    --wine-soft: #c9658f;
    --wine-pale: #f1d3e0;
  }
  * { margin: 0; padding: 0; box-sizing: border-box; }
  html, body {
    width: 1200px;
    height: 900px;
    overflow: hidden;
    background: var(--backdrop);
    font-family: "Quicksand", sans-serif;
  }
  .canvas {
    width: 1200px;
    height: 900px;
    display: flex;
    align-items: center;
    justify-content: center;
  }
  .business-card {
    position: relative;
    width: 1000px;
    height: 572px;
    background: var(--card);
    box-shadow: 0 10px 30px rgba(0,0,0,0.12);
    overflow: hidden;
  }
  .wine-stain {
    position: absolute;
    left: -40px;
    top: -60px;
    width: 360px;
    height: 330px;
    border-radius: 50%;
    background: radial-gradient(circle at 60% 55%, var(--wine-soft) 0%, var(--wine-pale) 45%, rgba(255,255,255,0) 70%);
  }
  .brand-name {
    position: absolute;
    left: 400px;
    top: 110px;
    font-size: 56px;
    font-weight: 400;
    letter-spacing: 4px;
    color: var(--ink);
    text-transform: uppercase;
    white-space: nowrap;
  }
  .holder-name {
    position: absolute;
    left: 62px;
    top: 284px;
    font-size: 40px;
    font-weight: 700;
    letter-spacing: 2px;
    color: var(--ink);
    white-space: nowrap;
  }
  .holder-name .first { color: var(--wine); }
  .contact-list {
    position: absolute;
    left: 540px;
    top: 272px;
    list-style: none;
  }
  .contact-item {
    display: flex;
    align-items: center;
    height: 44px;
    margin-bottom: 20px;
    font-size: 24px;
    font-weight: 500;
    letter-spacing: 1px;
    color: var(--ink);
    white-space: nowrap;
  }
  .contact-icon {
    width: 40px;
    height: 40px;
    margin-right: 22px;
    flex-shrink: 0;
  }
</style>
</head>
<body>
<main class="canvas">
  <section class="business-card">
    <div class="wine-stain" role="img" aria-label="Splashed wine ring stain with droplets"></div>

    <h1 class="brand-name">Copper Ladle</h1>

    <p class="holder-name"><span class="first">NAME</span> SURNAME</p>

    <ul class="contact-list">
      <li class="contact-item">
        <svg class="contact-icon" viewBox="0 0 42 42" fill="none" stroke="var(--wine)" stroke-width="3" stroke-linejoin="round" aria-hidden="true">
          <path d="M9 5 L15 5 L18 13 L14 17 C16 23 20 27 26 29 L30 25 L38 28 L38 34 C38 37 35 39 32 38 C18 35 7 24 4 10 C3 7 6 5 9 5 Z"/>
        </svg>
        014 0582 316
      </li>
      <li class="contact-item">
        <svg class="contact-icon" viewBox="0 0 42 42" fill="none" stroke="var(--wine)" stroke-width="3" stroke-linejoin="round" aria-hidden="true">
          <rect x="3" y="9" width="36" height="25"/>
          <path d="M3 9 L21 24 L39 9"/>
        </svg>
        hello@copperladle.com
      </li>
      <li class="contact-item">
        <svg class="contact-icon" viewBox="0 0 42 42" fill="none" stroke="var(--wine)" stroke-width="3" aria-hidden="true">
          <circle cx="21" cy="21" r="18"/>
          <ellipse cx="21" cy="21" rx="8" ry="18"/>
          <line x1="3" y1="21" x2="39" y2="21"/>
          <line x1="6" y1="12" x2="36" y2="12"/>
          <line x1="6" y1="30" x2="36" y2="30"/>
          <line x1="21" y1="3" x2="21" y2="39"/>
        </svg>
        www.copperladledenholt.com
      </li>
    </ul>
  </section>
</main>
</body>
</html>
```